Marlow Hire Business Card for recruitment company

We are looking for a Business Card Design that incorporates our personal details and our busines name and logo. We are a specialized search consultancy that recruit Property and Construction professionals.
We would like a business card that stands out and is appealing to the Construction and Property industry as well.

Target Market(s)

people in the construction and property industry

Contact Information for Business Card

Business Name and logo

Font styles to use
Serif

Colors
0094D4
00A9DD
6FCCEA
C7EBF8
E9F6FB

Requirements
Must have
• Business name and logo as well as contact details
Should not have
• No photos of us please

```html
<!DOCTYPE html>
<html lang="en">
<head>
<meta charset="utf-8">
<title>Marlow Hire – Business Card</title>
<link rel="stylesheet" href="https://fonts.googleapis.com/css2?family=Lora:wght@400;600&display=swap">
<style>
  :root {
    --page-bg: #eef1f2;
    --blue-deep: #0a5f8c;
    --blue-strong: #0094d4;
    --blue-bright: #00a9dd;
    --blue-soft: #6fccea;
    --blue-pale: #c7ebf8;
    --blue-mist: #e9f6fb;
    --text-on-blue: #e9f6fb;
    --text-name: #ffffff;
    --brand-ink: #0a4a6e;
  }
  * { margin: 0; padding: 0; box-sizing: border-box; }
  html, body {
    width: 1200px;
    height: 969px;
    overflow: hidden;
    background: var(--page-bg);
    font-family: "Lora", serif;
  }
  .card {
    position: absolute;
    left: 186px;
    top: 226px;
    width: 867px;
    height: 494px;
    border-radius: 22px;
    overflow: hidden;
    background: linear-gradient(150deg, var(--blue-mist), var(--blue-pale));
    box-shadow: 0 10px 30px rgba(10, 60, 90, 0.18);
  }
  .card__shape {
    position: absolute;
    inset: 0;
    width: 100%;
    height: 100%;
  }
  .contact {
    position: absolute;
    left: 70px;
    top: 110px;
    color: var(--text-on-blue);
  }
  .contact__name {
    font-size: 26px;
    font-weight: 600;
    letter-spacing: 0.5px;
    color: var(--text-name);
    line-height: 32px;
  }
  .contact__title {
    font-size: 18px;
    line-height: 22px;
  }
  .contact__divider {
    font-size: 16px;
    line-height: 16px;
    margin: 6px 0 8px;
    letter-spacing: 1px;
  }
  .contact__address {
    font-size: 18px;
    line-height: 24px;
    padding-left: 2px;
  }
  .contact__list { list-style: none; padding-left: 2px; }
  .contact__item {
    display: flex;
    align-items: center;
    gap: 12px;
    font-size: 18px;
    line-height: 24.5px;
  }
  .contact__icon { width: 16px; height: 16px; fill: var(--text-on-blue); flex: none; }
  .brand {
    position: absolute;
    left: 440px;
    top: 236px;
    width: 400px;
    display: flex;
    align-items: center;
    justify-content: center;
    gap: 14px;
  }
  .brand__mark {
    width: 30px;
    height: 30px;
    border-radius: 50%;
    background: var(--blue-strong);
    flex: none;
  }
  .brand__name {
    font-size: 42px;
    font-weight: 400;
    letter-spacing: 1px;
    color: var(--brand-ink);
    white-space: nowrap;
    line-height: 48px;
  }
</style>
</head>
<body>
  <div class="card">
    <svg class="card__shape" viewBox="0 0 867 494" aria-hidden="true">
      <defs>
        <linearGradient id="panelGradient" x1="0" y1="0" x2="1" y2="0.5">
          <stop offset="0" stop-color="var(--blue-strong)"/>
          <stop offset="1" stop-color="var(--blue-deep)"/>
        </linearGradient>
        <mask id="circleCut">
          <rect width="867" height="494" fill="#fff"/>
          <circle cx="634" cy="262" r="234" fill="#000"/>
        </mask>
      </defs>
      <path d="M0 0 H730 L696 40 L480 330 L364 494 H0 Z" fill="url(#panelGradient)" mask="url(#circleCut)"/>
      <circle cx="634" cy="262" r="234" fill="none" stroke="var(--blue-soft)" stroke-width="3"/>
    </svg>

    <div class="contact">
      <div class="contact__name">DANIEL HART</div>
      <div class="contact__title">President</div>
      <div class="contact__divider">-------</div>
      <div class="contact__address">412 Alder Court<br>Fairbanks, Alaska 99701</div>
      <div class="contact__divider">-------</div>
      <ul class="contact__list">
        <li class="contact__item">
          <svg class="contact__icon" viewBox="0 0 16 16"><path d="M3.5 1 6 3.5 4.7 5.4c.8 1.9 2.2 3.3 4 4.1L10.6 8 15 10.5 13.8 14C7.5 14.5 1.5 8.5 2 2.2Z"/></svg>
          555-214-7730</li>
        <li class="contact__item">
          <svg class="contact__icon" viewBox="0 0 16 16"><path d="M4 0h8a1 1 0 0 1 1 1v14a1 1 0 0 1-1 1H4a1 1 0 0 1-1-1V1a1 1 0 0 1 1-1Zm1 2v10h6V2Zm3 11a1 1 0 1 0 0 2 1 1 0 0 0 0-2Z"/></svg>
          555-318-6042</li>
        <li class="contact__item">
          <svg class="contact__icon" viewBox="0 0 16 16"><path d="M4 1h6l2 2v3H4Zm-3 6h14v6h-2v-3H3v3H1Zm3 4h8v4H4Z"/></svg>
          555-406-2291</li>
        <li class="contact__item">
          <svg class="contact__icon" viewBox="0 0 16 16"><path d="M1 3h14v10H1Zm1.5 1.2L8 8.5l5.5-4.3Z"/></svg>
          daniel@marlowhire.com</li>
        <li class="contact__item">
          <svg class="contact__icon" viewBox="0 0 16 16"><path d="M8 1a7 7 0 1 0 0 14A7 7 0 0 0 8 1Zm-2 3 2 1 1 2-2 1 1 3-2 1-1-3-2-2 2-2Zm5 1 2 2-1 3-2-1V6Z"/></svg>
          www.marlowhire.com</li>
      </ul>
    </div>

    <div class="brand">
      <span class="brand__mark" aria-hidden="true"></span>
      <span class="brand__name">MARLOW HIRE</span>
    </div>
  </div>
</body>
</html>
```